BEACON CABS

Taxi card design

Need changes very slow in replying to my messages.

Target Market(s)

Customers

Industry/Entity Type

Taxi

Contact Information for Business Card

See previous design

Font styles to use
Sans Serif

Colors
A7469A
B969AE
D3A5CF
EDDBEB
F8F0F9
6B429C
8869AF
B7A5CE
E3DAEB
F3F0F8

Requirements
Nice to have
• We are in the business of looking after people, not just driving vehicles front
Should not have
• Front number 01632 480 480 needs to big big

```html
<!DOCTYPE html>
<html lang="en">
<head>
<meta charset="utf-8">
<title>Beacon Cabs – Business Card</title>
<link href="https://fonts.googleapis.com/css2?family=Open+Sans:wght@400;600;700;800&family=PT+Sans+Narrow:wght@700&display=swap" rel="stylesheet">
<style>
  :root {
    --violet: #6B429C;
    --magenta: #A7469A;
    --paper: #f6f5f6;
    --ink: #1a1a1a;
    --navy: #1d3550;
    --white: #ffffff;
    --brand-gradient: linear-gradient(90deg, var(--violet), var(--magenta));
    --brand-gradient-rev: linear-gradient(90deg, var(--magenta), var(--violet));
  }
  * { margin: 0; padding: 0; box-sizing: border-box; }
  html, body {
    width: 1200px; height: 1200px; overflow: hidden;
    background: var(--white);
    font-family: "Open Sans", sans-serif;
  }
  .card {
    position: absolute; left: 263px; width: 675px; height: 405px;
    background: var(--paper); overflow: hidden;
  }
  .card--front { top: 97px; }
  .card--back { top: 697px; }

  /* FRONT */
  .front-panel {
    position: absolute; inset: 0;
    background: var(--brand-gradient);
    clip-path: polygon(0 0, 403px 0, 294px 100%, 0 100%);
  }
  .brand {
    position: absolute; left: 47px; top: 64px; width: 290px;
    color: var(--white);
  }
  .brand__name {
    font-weight: 800; font-size: 40px; letter-spacing: -0.5px; line-height: 1;
  }
  .brand__since {
    font-size: 10.5px; font-weight: 600; margin-top: 4px; padding-left: 36px;
  }
  .brand__service {
    position: absolute; left: 215px; top: 125px;
    color: var(--white); font-weight: 700; font-size: 20px;
  }
  .main-phone {
    position: absolute; left: 64px; top: 194px;
    display: flex; align-items: center; gap: 8px;
    color: var(--white); font-weight: 700; font-size: 31px; letter-spacing: 0.5px;
  }
  .icon-phone { width: 22px; height: 22px; flex: none; }
  .alt-phones {
    position: absolute; left: 46px; top: 252px;
    display: flex; flex-direction: column; gap: 5px;
  }
  .alt-phone {
    width: 217px; height: 31px; border-radius: 8px;
    background: var(--white); color: var(--violet);
    display: flex; align-items: center; gap: 5px; padding-left: 8px;
    font-family: "PT Sans Narrow", sans-serif; font-weight: 700; font-size: 28px;
  }
  .alt-phone .icon-phone { width: 19px; height: 19px; }

  .services {
    position: absolute; left: 399px; top: 45px;
    display: flex; flex-direction: column; gap: 4px;
  }
  .service {
    width: 231px; height: 40px;
    background: var(--brand-gradient-rev);
    border-radius: 10px 10px 0 10px;
    color: var(--white); font-size: 20px; text-transform: uppercase;
    display: flex; align-items: center; justify-content: center;
  }
  .service:first-child { background: var(--brand-gradient); }
  .service:last-child { background: var(--brand-gradient); }

  .contact {
    position: absolute; left: 397px; top: 197px;
    list-style: none; font-size: 16.5px; color: var(--ink);
  }
  .contact__row { display: flex; align-items: flex-start; gap: 9px; margin-bottom: 6px; }
  .contact__icon { width: 20px; height: 20px; flex: none; color: var(--violet); }
  .contact__address { color: var(--navy); line-height: 21px; margin-top: -1px; }

  /* BACK */
  .band { position: absolute; left: 0; right: 0; }
  .band--top { top: 0; height: 86px; background: var(--brand-gradient); }
  .band--top-rule { top: 90px; height: 4px; background: var(--brand-gradient-rev); }
  .band--bottom-rule { top: 312px; height: 4px; background: var(--brand-gradient); }
  .band--bottom {
    top: 318px; bottom: 0; background: var(--brand-gradient-rev);
    display: flex; justify-content: center; padding-top: 6px;
  }
  .back-phone {
    display: flex; align-items: center; gap: 6px; height: 30px;
    color: var(--white); font-weight: 700; font-size: 24px; letter-spacing: 0.5px;
  }
  .back-phone .icon-phone { width: 18px; height: 18px; }
  .back-brand {
    position: absolute; left: 0; right: 0; top: 170px; text-align: center;
    font-weight: 800; font-size: 48px; color: var(--ink); letter-spacing: -0.5px;
  }
</style>
</head>
<body>
<svg width="0" height="0" style="position:absolute" aria-hidden="true">
  <symbol id="phone-tile" viewBox="0 0 24 24">
    <rect x="1" y="1" width="22" height="22" rx="5" fill="currentColor"/>
    <path d="M7.5 5.5c-.8.4-1.6 1.3-1.5 2.6.3 4.2 5.4 9.6 9.7 10 1.3.1 2.2-.6 2.6-1.4l-2.4-2.1-1.6 1.2c-2-1-3.7-2.8-4.6-4.8l1.2-1.5L8.8 7z" fill="var(--tile-ink, #fff)"/>
    <path d="M13.5 6.5a4 4 0 0 1 4 4M13.5 4a6.5 6.5 0 0 1 6.5 6.5" stroke="var(--tile-ink, #fff)" stroke-width="1.3" fill="none" stroke-linecap="round"/>
  </symbol>
</svg>

<section class="card card--front">
  <div class="front-panel"></div>

  <div class="brand">
    <div class="brand__name">Beacon Cabs</div>
    <div class="brand__since">Established since 1986</div>
  </div>
  <div class="brand__service">24/7 Service</div>

  <div class="main-phone">
    <svg class="icon-phone" style="color:#fff;--tile-ink:var(--violet)"><use href="#phone-tile"/></svg>
    01632 480 480
  </div>

  <div class="alt-phones">
    <div class="alt-phone"><svg class="icon-phone" style="color:var(--violet)"><use href="#phone-tile"/></svg>01632 96 55 55</div>
    <div class="alt-phone"><svg class="icon-phone" style="color:var(--violet)"><use href="#phone-tile"/></svg>01632 30 30 30</div>
    <div class="alt-phone"><svg class="icon-phone" style="color:var(--violet)"><use href="#phone-tile"/></svg>01632 96 11 88</div>
  </div>

  <div class="services">
    <div class="service">Airport Transfers</div>
    <div class="service">Minibuses</div>
    <div class="service">School Transport</div>
  </div>

  <ul class="contact">
    <li class="contact__row">
      <svg class="contact__icon" viewBox="0 0 24 24"><path d="M6 3c-1.2.5-2.5 1.9-2.3 3.9.5 6.4 7.7 13.6 14 14.2 2 .2 3.3-1 3.8-2.2l-3.6-3.2-2.4 1.8c-3-1.5-5.5-4-7-7l1.8-2.3z" fill="currentColor"/><path d="M14 5a5 5 0 0 1 5 5M14 1.5a8.5 8.5 0 0 1 8.5 8.5" stroke="currentColor" stroke-width="1.6" fill="none" stroke-linecap="round"/></svg>
      <span>0800 555 0 111</span>
    </li>
    <li class="contact__row">
      <svg class="contact__icon" viewBox="0 0 24 24"><circle cx="12" cy="12" r="4" fill="none" stroke="currentColor" stroke-width="2.4"/><path d="M16 8v5.5c0 2 3.5 2 3.5-1.5A7.5 7.5 0 1 0 15 19" fill="none" stroke="currentColor" stroke-width="2.4" stroke-linecap="round"/></svg>
      <span>beaconcabs@mailbox.example</span>
    </li>
    <li class="contact__row">
      <svg class="contact__icon" viewBox="0 0 24 24"><circle cx="12" cy="12" r="9" fill="none" stroke="currentColor" stroke-width="2"/><path d="M3 12h18M12 3c-3 3-3 15 0 18M12 3c3 3 3 15 0 18M5 7.5h14M5 16.5h14" fill="none" stroke="currentColor" stroke-width="1.6"/></svg>
      <span>www.beaconcabs.example</span>
    </li>
    <li class="contact__row">
      <svg class="contact__icon" viewBox="0 0 24 24"><path d="M12 2a7 7 0 0 0-7 7c0 5 7 13 7 13s7-8 7-13a7 7 0 0 0-7-7z" fill="currentColor"/><circle cx="12" cy="9" r="2.6" fill="#fff"/></svg>
      <span class="contact__address">Kestrel Hall<br>Millgate Rd<br>Ashbridge<br>AB12 3CD</span>
    </li>
  </ul>
</section>

<section class="card card--back">
  <div class="band band--top"></div>
  <div class="band band--top-rule"></div>
  <div class="back-brand">Beacon Cabs</div>
  <div class="band band--bottom-rule"></div>
  <div class="band band--bottom">
    <div class="back-phone">
      <svg class="icon-phone" style="color:#fff;--tile-ink:var(--magenta)"><use href="#phone-tile"/></svg>
      01632 480 480
    </div>
  </div>
</section>
</body>
</html>
```